25kg bag for branded milk powder

We are looking for an attractive bag for our Holland dairy milk powder range. We will have 5 kinds of products.

Instant Full Cream milk powder
Full cream milk powder
Instant fat filled milk powder
Skimmed milk powder
Dairy ingredients

The bags are standard industrial 25kg kraft multiply paper bags with inner poly linner.

We want to have an hormonized design where each type of dairy product is differentiated by the product name and a color,

Please see attached design as reference.

Target Market(s)

Middle East and Africa

Font styles to use
Sans Serif

Requirements
Must have
• The bags must show that we are a dutch company and have a profesional feel.
• We want a general design that will be differentiated by colour coding.
• We want the design to be less conservative compared to the attached examples.
• The bags must be easilly recognisable from all sides as for picture of Vorlund Creameries branded bags on pallets attached.
• We have also attached some bags design templates as a reference.
Nice to have
• We would like to use sybols or imagery that symbolises Dutch origin and quality
Should not have
• We cannot have too many images to keep it simple.

```html
<!DOCTYPE html>
<html lang="en">
<head>
<meta charset="utf-8">
<title>Veldmeer Dairy Foods – Milk Powder 25kg Bag</title>
<link href="https://fonts.googleapis.com/css2?family=Baloo+2:wght@800&family=Montserrat:wght@500;600;700&display=swap" rel="stylesheet">
<style>
  :root{
    --bg:#ededed;
    --bag:#ffffff;
    --blue:#1f7fd6;
    --blue-dark:#0d5fb0;
    --orange:#f5a100;
    --ink:#333333;
    --green:#2f8f2a;
    --green-light:#56b63a;
    --green-dark:#1f6e1e;
    --rib-red:#e8412a;
    --rib-orange:#f39a1e;
    --rib-blue:#25a6dc;
    --rib-lime:#a6c62a;
  }
  *{margin:0;padding:0;box-sizing:border-box}
  html,body{width:1200px;height:800px;overflow:hidden;background:var(--bg)}
  .canvas{position:relative;width:1200px;height:800px;background:var(--bg)}
  .bag-face{
    position:absolute;left:375px;top:40px;width:450px;height:720px;
    background:var(--bag);overflow:hidden;
    box-shadow:0 10px 30px rgba(0,0,0,.12);
    font-family:'Montserrat',sans-serif;
  }
  .brand{position:absolute;top:46px;left:0;width:100%;text-align:center}
  .brand-mark{display:inline-block;width:26px;height:26px;border-radius:50%;background:var(--orange);vertical-align:middle;margin-right:8px}
  .brand-name{display:inline-block;vertical-align:middle;font-weight:700;font-size:26px;color:var(--orange);letter-spacing:1px}
  .brand-sub{display:block;margin-top:4px;font-weight:500;font-size:14px;letter-spacing:4px;color:var(--ink)}
  .product{
    position:absolute;top:120px;left:0;width:100%;text-align:center;
    font-family:'Baloo 2',sans-serif;font-weight:800;font-size:140px;line-height:1;
    color:var(--blue);
  }
  .product-type{
    position:absolute;top:290px;left:0;width:100%;text-align:center;
    font-weight:500;font-size:28px;letter-spacing:16px;color:var(--blue);
    padding-left:16px;
  }
  .fat-list{
    position:absolute;top:395px;left:30px;list-style:none;
    font-weight:700;font-size:13px;line-height:1.35;color:var(--blue-dark);
  }
  .benefits{position:absolute;top:385px;right:24px;width:150px;list-style:none}
  .benefits li{
    height:20px;margin-bottom:3px;padding-left:14px;
    font-weight:700;font-size:11px;line-height:20px;letter-spacing:1px;color:#fff;
    clip-path:polygon(4% 0,100% 0,97% 100%,0 100%);
  }
  .benefits .protein{background:var(--rib-red)}
  .benefits .iron{background:var(--rib-orange)}
  .benefits .calcium{background:var(--rib-blue)}
  .benefits .vitamins{background:var(--rib-lime)}
  .landscape{position:absolute;left:0;bottom:0;width:450px;height:250px}
  .weight{
    position:absolute;left:28px;bottom:24px;
    font-weight:600;font-size:30px;color:#fff;letter-spacing:1px;
  }
</style>
</head>
<body>
<div class="canvas">
  <div class="bag-face">
    <div class="brand">
      <span class="brand-mark"></span><span class="brand-name">Veldmeer</span>
      <span class="brand-sub">Dairy Foods</span>
    </div>

    <div class="product">Milk</div>
    <div class="product-type">powder</div>

    <ul class="fat-list">
      <li>FAT 1.5 %</li>
      <li>FAT 3.2 %</li>
      <li>LOW FAT 0.2 %</li>
    </ul>

    <ul class="benefits">
      <li class="protein">PROTIEN</li>
      <li class="iron">IRON</li>
      <li class="calcium">CALCIUM</li>
      <li class="vitamins">VITAMINS</li>
    </ul>

    <svg class="landscape" viewBox="0 0 450 250" role="img" aria-label="Green Dutch pasture with windmills and grazing cow silhouettes">
      <defs>
        <linearGradient id="meadow" x1="0" y1="0" x2="0" y2="1">
          <stop offset="0" stop-color="var(--green-light)"/>
          <stop offset="1" stop-color="var(--green)"/>
        </linearGradient>
      </defs>
      <path d="M0 20 C110 0 240 30 450 70 L450 250 L0 250 Z" fill="url(#meadow)"/>
      <path d="M0 90 C140 95 290 130 450 175 L450 195 C290 150 140 118 0 112 Z" fill="#ffffff"/>
      <path d="M0 112 C140 118 290 150 450 195 L450 250 L0 250 Z" fill="var(--green-dark)"/>
    </svg>

    <div class="weight">25kg</div>
  </div>
</div>
</body>
</html>
```